Brindle Deals is an online marketing platform

A daily deals site for consumers a way to bring in new clients for clients and this is who the business cards are for. Industries - Food and Drink, Things To Do, Beauty and Spas, Staycations and Services.This leaflet is going to be used to get member of the public to sign up to our website

```html
<!DOCTYPE html>
<html lang="en">
<head>
<meta charset="utf-8">
<title>Brindle Deals – Sign-up Leaflet</title>
<link rel="stylesheet" href="https://fonts.googleapis.com/css2?family=Oswald:wght@500;600&family=Caveat:wght@700&family=Gochi+Hand&family=Jost:wght@600&display=swap">
<style>
  :root {
    --backdrop: #bdbdbd;
    --brand-blue: #0d4fa0;
    --deep-blue: #083d80;
    --sky: #93b4d8;
    --lake: #2f6f8c;
    --accent-yellow: #e2e400;
    --bubble-yellow: #d6dc00;
    --ink: #111111;
    --paper: #ffffff;
    --form-grey: #e9ecf1;
  }
  * { box-sizing: border-box; margin: 0; padding: 0; }
  html, body { width: 1200px; height: 900px; overflow: hidden; }
  body { background: var(--backdrop); position: relative; }

  .leaflet {
    position: absolute; left: 400px; top: 30px;
    width: 400px; height: 840px;
    background: var(--brand-blue);
    overflow: hidden;
  }

  .hero-photo {
    position: absolute; left: 0; top: 60px; width: 400px; height: 480px;
    background: linear-gradient(to bottom, var(--sky) 0%, #6f93c0 30%, var(--lake) 62%, var(--brand-blue) 100%);
  }

  .brand-tab {
    position: absolute; left: 118px; top: 0; width: 225px; height: 96px;
    background: var(--paper);
    border-right: 6px solid var(--deep-blue);
    border-bottom: 4px solid var(--deep-blue);
    display: flex; align-items: center; justify-content: center; gap: 10px;
  }
  .brand-tab__dot { width: 26px; height: 26px; border-radius: 50%; background: var(--brand-blue); }
  .brand-tab__name {
    font-family: "Jost", sans-serif; font-weight: 600; font-size: 26px;
    color: var(--brand-blue); letter-spacing: 0.5px;
  }

  .headline {
    position: absolute; left: 20px; top: 108px; width: 360px;
    font-family: "Caveat", cursive; font-weight: 700; font-size: 40px; line-height: 0.95;
    text-align: center; color: var(--paper);
    text-shadow: 2px 2px 0 var(--brand-blue), -1px -1px 0 var(--brand-blue), 1px -1px 0 var(--brand-blue), -1px 1px 0 var(--brand-blue);
  }

  .callout {
    position: absolute;
    font-family: "Oswald", sans-serif; font-weight: 600; text-transform: uppercase;
    color: var(--accent-yellow); line-height: 0.95; text-align: center;
  }
  .callout--prize { left: 18px; top: 300px; width: 140px; font-size: 28px; }
  .callout--register { left: 205px; top: 238px; width: 185px; font-size: 26px; }
  .callout__url { display: block; font-size: 20px; white-space: nowrap; margin-top: 2px; }

  .pointer-arrow { position: absolute; left: 140px; top: 300px; width: 120px; height: 80px; }

  .offer-bubble { position: absolute; left: 20px; top: 392px; width: 370px; height: 260px; }
  .offer-bubble__text {
    position: absolute; left: 70px; top: 432px; width: 270px;
    font-family: "Gochi Hand", cursive; font-size: 22px; line-height: 1.2;
    color: var(--ink); text-align: center;
  }

  .launch {
    position: absolute; left: 20px; top: 640px; width: 360px;
    font-family: "Oswald", sans-serif; font-weight: 600; font-size: 25px; line-height: 1;
    text-transform: uppercase; text-align: center; color: var(--paper);
  }
  .launch__date { color: var(--accent-yellow); }
  .launch sup { font-size: 13px; }

  .entry-panel {
    position: absolute; left: 212px; top: 722px; width: 188px; height: 118px;
    background: var(--form-grey);
    clip-path: polygon(0 20%, 100% 0, 100% 100%, 0 100%);
  }
  .entry-form {
    position: absolute; left: 222px; top: 752px; width: 170px; height: 82px;
    border: 2px dashed var(--brand-blue); padding: 5px 8px;
    font-family: "Oswald", sans-serif; font-weight: 500; font-size: 8px;
    color: var(--deep-blue); text-transform: uppercase;
  }
  .entry-form__field { border-bottom: 1px dotted var(--brand-blue); height: 12px; line-height: 12px; }
  .entry-form__optout { display: flex; gap: 5px; margin-top: 4px; font-size: 6px; line-height: 1.2; }
  .entry-form__box { flex: 0 0 10px; height: 10px; border: 1.5px solid var(--brand-blue); background: var(--paper); }

  .entry-prompt {
    position: absolute; left: 14px; top: 762px; width: 190px; height: 66px;
    border: 2px dashed var(--accent-yellow);
    display: flex; align-items: center; justify-content: center;
    font-family: "Oswald", sans-serif; font-weight: 500; font-size: 11px; line-height: 1.15;
    text-transform: uppercase; text-align: center; color: var(--paper); padding: 4px 8px;
  }
</style>
</head>
<body>
  <main class="leaflet">
    <div class="hero-photo" role="img" aria-label="Photo of a person leaping joyfully into a calm lake surrounded by green wooded hills"></div>

    <header class="brand-tab">
      <span class="brand-tab__dot"></span>
      <span class="brand-tab__name">Brindle Deals</span>
    </header>

    <h1 class="headline">The best experiences the South West has to offer</h1>

    <p class="callout callout--prize">You want to win £200 to explore?</p>
    <p class="callout callout--register">Register for free now at <span class="callout__url">brindledeals.co.uk</span></p>

    <svg class="pointer-arrow" viewBox="0 0 120 80" aria-hidden="true">
      <path d="M10 60 Q40 80 70 55 L95 25" fill="none" stroke="var(--accent-yellow)" stroke-width="5" stroke-linecap="round"/>
      <path d="M78 22 L100 18 L98 42" fill="none" stroke="var(--accent-yellow)" stroke-width="5" stroke-linecap="round" stroke-linejoin="round"/>
    </svg>

    <svg class="offer-bubble" viewBox="0 0 370 260" aria-hidden="true">
      <polygon points="20,40 350,10 335,190 230,195 205,245 185,198 60,200"
               fill="var(--bubble-yellow)" stroke="var(--ink)" stroke-width="5" stroke-linejoin="round"/>
    </svg>
    <p class="offer-bubble__text">We gives you access to exciting offers across the best restaurants, hotels, spas, leisure activities &amp; services.</p>

    <p class="launch">
      <span class="launch__date">Launching on the 1<sup>st</sup> August 2019</span> – be the first to receive exclusive offers and win!
    </p>

    <div class="entry-panel"></div>
    <form class="entry-form">
      <div class="entry-form__field">Name:</div>
      <div class="entry-form__field">Email:</div>
      <div class="entry-form__field">Mobile:</div>
      <div class="entry-form__field">Address:</div>
      <div class="entry-form__optout">
        <span class="entry-form__box"></span>
        <span>Please tick here if you would not like to receive updates on fabulous offers and new experiences.</span>
      </div>
    </form>

    <p class="entry-prompt">Complete your details here for your chance to win and be the first to receive fresh fancy offers just for you.</p>
  </main>
</body>
</html>
```